Varemo Group Business Card Design

The CEO is looking for a new trendy look for his business card.
You can stay with current branding or come up with something new/creative. It can be 3D, including Medical Office buildings. You can use our logo in a variety of colors. Please include name, title, company name, company website, email address, cell number

Target Market(s)

Real Estate Development and Construction

Industry/Entity Type

Health care real estate

Contact Information for Business Card

Rohesh Kumbar, CEO M-727.418.9062 E-roheshkumbar@varemo.com Address:4100 Lindell Ave, Tampa, FL 33611 www.varemo.com

Font styles to use
Other font styles liked:
• Be creative

Requirements
Must have
• Creative, trendy look
Nice to have
• Please go to our website to get a feel- www. varemo.com
Should not have
• small fonts

```html
<!DOCTYPE html>
<html lang="en">
<head>
<meta charset="utf-8">
<title>Varemo Group – Business Card</title>
<link rel="stylesheet" href="https://fonts.googleapis.com/css2?family=Archivo+Black&family=Roboto+Slab:wght@400;500&display=swap">
<style>
  :root {
    --backdrop: #6e6e6e;
    --card: #111111;
    --card-edge: #1c1c1c;
    --pattern-dark: #161616;
    --pattern-light: #1f1f1f;
    --red: #b3151b;
    --white: #f2f2f2;
  }
  * { margin: 0; padding: 0; box-sizing: border-box; }
  html, body {
    width: 1200px; height: 911px; overflow: hidden;
    background: var(--backdrop);
  }
  .stage {
    width: 1200px; height: 911px;
    display: flex; align-items: center; justify-content: center; gap: 40px;
  }
  .card {
    position: relative;
    width: 540px; height: 309px;
    background: var(--card);
    border: 1px solid var(--card-edge);
    box-shadow: 0 18px 40px rgba(0,0,0,.35);
    overflow: hidden;
  }
  /* back of card */
  .card-back__pattern {
    position: absolute; inset: 0;
    background: linear-gradient(135deg, var(--pattern-dark) 0%, var(--pattern-light) 55%, var(--pattern-dark) 100%);
  }
  .card-back__brand {
    position: absolute; right: 40px; bottom: 34px;
    font-family: "Archivo Black", sans-serif;
    font-size: 22px; color: var(--red); letter-spacing: -0.5px;
  }
  /* front of card */
  .brand {
    position: absolute; left: 38px; top: 62px;
    font-family: "Archivo Black", sans-serif;
    font-size: 30px; line-height: 1; color: var(--red);
    letter-spacing: -1px; white-space: nowrap;
  }
  .person {
    position: absolute; right: 44px; top: 116px; text-align: right;
    white-space: nowrap;
  }
  .person__name {
    font-family: "Archivo Black", sans-serif;
    font-size: 20px; line-height: 1.1; color: var(--red); letter-spacing: 0.5px;
    text-transform: uppercase;
  }
  .person__title {
    font-family: "Roboto Slab", serif; font-weight: 500;
    font-size: 13px; color: var(--white); margin-top: 4px;
  }
  .accent-triangle {
    position: absolute; right: 0; top: 104px; width: 20px; height: 40px;
  }
  .contact {
    position: absolute; left: 38px; bottom: 34px;
    font-family: "Roboto Slab", serif; font-size: 13px;
    color: var(--white); line-height: 1.55;
  }
  .contact__address { margin-bottom: 4px; }
  .contact__row { display: flex; align-items: center; gap: 9px; }
  .contact__icon { width: 12px; height: 12px; flex: none; }
</style>
</head>
<body>
<main class="stage">
  <section class="card card-back" aria-label="Card back">
    <div class="card-back__pattern" role="img" aria-label="Tone-on-tone black pattern of repeated company wordmarks"></div>
    <div class="card-back__brand">Varemo</div>
  </section>

  <section class="card card-front" aria-label="Card front">
    <div class="brand">Varemo Group</div>

    <div class="person">
      <div class="person__name">Rohesh Kumbar</div>
      <div class="person__title">President / CEO</div>
    </div>
    <svg class="accent-triangle" viewBox="0 0 20 40" aria-hidden="true">
      <polygon points="20,0 20,40 0,20" fill="var(--red)"/>
    </svg>

    <div class="contact">
      <p class="contact__address">4100 Lindell Avenue<br>Tampa, FL 33611</p>
      <p class="contact__row">
        <svg class="contact__icon" viewBox="0 0 12 12" aria-hidden="true"><rect x="3" y="0.8" width="6" height="10.4" rx="1" fill="none" stroke="var(--red)" stroke-width="1.3"/><circle cx="6" cy="9.2" r=".7" fill="var(--red)"/></svg>
        727.418.9062
      </p>
      <p class="contact__row">
        <svg class="contact__icon" viewBox="0 0 12 12" aria-hidden="true"><rect x="0.7" y="2.2" width="10.6" height="7.6" fill="none" stroke="var(--red)" stroke-width="1.3"/><polyline points="0.7,2.2 6,6.6 11.3,2.2" fill="none" stroke="var(--red)" stroke-width="1.3"/></svg>
        roheshkumbar@varemo.com
      </p>
      <p class="contact__row">
        <svg class="contact__icon" viewBox="0 0 12 12" aria-hidden="true"><circle cx="6" cy="6" r="5.2" fill="none" stroke="var(--red)" stroke-width="1.3"/><ellipse cx="6" cy="6" rx="2.2" ry="5.2" fill="none" stroke="var(--red)" stroke-width="1"/><line x1="0.8" y1="6" x2="11.2" y2="6" stroke="var(--red)" stroke-width="1"/></svg>
        www.varemo.com
      </p>
    </div>
  </section>
</main>
</body>
</html>
```